KV HOLDING Business Cards

I need business cards for "KV Holding group LLC" doublesided... logo on the back (also include logo on front)
logo attached to project... i have jpg up..
Company Info:
418 East Marlow Avenue, Suite 7B
Chicago, Illinois 60617
facsimile 312-555-0188 (list fax, address, website on all cards.)
www.kvholdinggroup.example
Three different people on cards:
Dorian P. Kell, CPA MST
Principal
ofc 312-555-0142
mobile 312-555-0167
dorianpkell@kvholdinggroup.example
Marcus T. Brenholt, CPA MST
Principal
marcustbrenholt@kvholdinggroup.example
mobile 708-555-0119
ofc 312-555-0142
Nigel F Carrow
Principal
ofc 312-555-0142
no mobile
nigelfcarrow@kvholdinggroup.example
I have multiple projects listed.. see below:
Business cards for amber gate equity llc
letterhead
envelopes
Business cards for KV Holding LLC
letterhead
envelopes
Target Market(s)
rich people
Industry/Entity Type
Business
Look and feel

```html
<!DOCTYPE html>
<html lang="en">
<head>
<meta charset="utf-8">
<title>KV Holding Group LLC – Business Cards</title>
<link rel="stylesheet" href="https://fonts.googleapis.com/css2?family=Open+Sans:wght@400;600&display=swap">
<style>
  :root {
    --page-bg: #e4e5e7;
    --navy: #173a78;
    --blue: #1f5ea8;
    --blue-light: #2c7cc4;
    --paper: #f3f4f6;
    --ink-name: #1c3b73;
    --ink-light: #ffffff;
    --card-shadow: rgba(20, 30, 50, 0.22);
  }
  * { box-sizing: border-box; margin: 0; padding: 0; }
  html, body {
    width: 1200px;
    height: 750px;
    overflow: hidden;
    background: var(--page-bg);
  }
  .sheet {
    position: relative;
    width: 1200px;
    height: 750px;
    display: flex;
    align-items: center;
    justify-content: center;
    gap: 60px;
  }
  .card {
    position: relative;
    width: 520px;
    height: 300px;
    border-radius: 28px;
    overflow: hidden;
    background: var(--paper);
    box-shadow: 0 10px 28px var(--card-shadow);
  }
  .card-shapes {
    position: absolute;
    inset: 0;
    width: 100%;
    height: 100%;
  }
  .company-name {
    position: absolute;
    font-family: "Open Sans", Arial, sans-serif;
    font-weight: 600;
    color: var(--ink-name);
    white-space: nowrap;
  }
  .card-front .company-name {
    left: 0;
    right: 0;
    top: 48px;
    text-align: center;
    font-size: 15px;
  }
  .card-back .company-name {
    left: 175px;
    top: 168px;
    font-size: 22px;
  }
  .contact {
    position: absolute;
    font-family: "Open Sans", Arial, sans-serif;
    color: var(--ink-light);
    font-size: 10.5px;
    line-height: 1.45;
  }
  .contact-person {
    left: 118px;
    top: 180px;
  }
  .contact-person .name { font-weight: 600; }
  .contact-company {
    left: 292px;
    top: 116px;
    padding-left: 12px;
    border-left: 1px solid rgba(255, 255, 255, 0.85);
  }
</style>
</head>
<body>
<main class="sheet">

  <section class="card card-front" aria-label="Business card, contact side">
    <svg class="card-shapes" viewBox="0 0 520 300" preserveAspectRatio="none" aria-hidden="true">
      <defs>
        <linearGradient id="frontBlue" x1="0" y1="1" x2="1" y2="0">
          <stop offset="0" stop-color="var(--blue-light)"/>
          <stop offset="0.55" stop-color="var(--blue)"/>
          <stop offset="1" stop-color="var(--navy)"/>
        </linearGradient>
      </defs>
      <rect width="520" height="300" fill="url(#frontBlue)"/>
      <path d="M0,52 Q250,10 520,22 L520,78 Q260,92 0,158 Z" fill="var(--paper)"/>
    </svg>

    <div class="company-name">KV Holding Group LLC</div>

    <div class="contact contact-person">
      <p class="name">Dorian P. Kell, CPA MST</p>
      <p>Principal</p>
      <p>ofc 312-555-0142</p>
      <p>mobile 312-555-0167</p>
      <p>dorianpkell@kvholdinggroup.example</p>
    </div>

    <div class="contact contact-company">
      <p>418 East Marlow Avenue, Suite 7B</p>
      <p>Chicago, Illinois 60617</p>
      <p>facsimile 312-555-0188</p>
      <p>www.kvholdinggroup.example</p>
    </div>
  </section>

  <section class="card card-back" aria-label="Business card, name side">
    <svg class="card-shapes" viewBox="0 0 520 300" preserveAspectRatio="none" aria-hidden="true">
      <defs>
        <linearGradient id="backBlue" x1="0" y1="1" x2="1" y2="0">
          <stop offset="0" stop-color="var(--navy)"/>
          <stop offset="0.5" stop-color="var(--blue)"/>
          <stop offset="1" stop-color="var(--navy)"/>
        </linearGradient>
      </defs>
      <rect width="520" height="300" fill="var(--paper)"/>
      <path d="M0,0 L520,0 L520,40 Q180,40 60,300 L0,300 Z" fill="url(#backBlue)"/>
    </svg>

    <div class="company-name">KV Holding Group LLC</div>
  </section>

</main>
</body>
</html>
```